3 Flyer Project: Industrial, Civil, and Commercial

Total of 3 separate flyers that go together to be put in folders for marketing. The three flyer categories will be Industrial, Civil, and Commercial. I will upload three photos for each flyer and verbiage for each flyer. The photos may change upon final revisions. We want creativity and not just bullet points on a page.

FLYER #1 INDUSTRIAL

INDUSTRIAL EXPERIENCE:
BRAVEMOOR UTILITIES
VELKAR
GRAYWICK QUARRY
ODELL FORGEWORKS
PELLMAN CRYSTALLINE
HARROWGATE & DUNMORE RAIL LINE

INDUSTRIAL FOCUS AREAS:
PLANT FACILITY WATER SYSTEMS
HEAVY CONCRETE
FACILITY REPAIR
INDUSTRIAL UPGRADES
RAILWAYS AND MANUFACTURING

INDUSTRIAL SOLUTIONS:
WE MAINTAIN AN EXTENSIVE LEVEL OF DETAIL AND INNOVATIVE PROBLEM-SOLVING TALENTS TO DELIVER HIGH QUALITY, SUSTAINABLE SOLUTIONS.

FLYER #2 CIVIL

CIVIL EXPERIENCE:
CORVANE DEPT. OF TRANSPORTATION
WEXLOW DEPT. OF TRANSPORTATION
TAVERLY DEPT. OF TRANSPORTATION
BUILDERS GUILD BOARD
NATIONAL FLIGHT SAFETY OFFICE
MINISTRY OF GUARDIANSHIP

CIVIL FOCUS AREAS:
AIRFIELD
STREETSCAPES
STORM DRAINAGE
UTILITY UPGRADES
BOX CULVERTS
RETAINING WALLS

CIVIL SOLUTIONS:
WE SPECIALIZE IN COMPLEX CIVIL PROJECTS.

FLYER #3 COMMERCIAL

COMMERCIAL EXPERIENCE:
HOLLISTER VALE UNIVERSITY
CORVANE OFFICE OF FACILITIES
TOWN OF BRANWICK, CORVANE
TOWN OF ELDERMOOR, CORVANE
ACADEMIC REGENTS COUNCIL

COMMERCIAL FOCUS AREAS:
NEW CONSTRUCTION
RENOVATIONS
STRUCTURAL FOUNDATIONS
STRUCTURAL UPGRADES

COMMERCIAL SOLUTIONS:
WE NOT ONLY KNOW HOW ALL THE PARTS AND PIECES FIT TOGETHER WITHIN A PROJECT, BUT WE SPECIALIZE IN THE SELF PERFORMANCE OF MANY DIVISIONS WHICH DIFFERENTIATES US FROM MANY OTHER GENERAL CONTRACTORS.

Marketing

• 3 photos on each flyer based on the Industrial, Commercial, and Civil flyers description. Our company logo as well as descriptions shown for each flyer. The blue we use in our logo cmyk is 100-80-0-22

```html
<!DOCTYPE html>
<html lang="en">
<head>
<meta charset="utf-8">
<title>Harwell Construction – Solutions Flyers</title>
<link href="https://fonts.googleapis.com/css2?family=Bebas+Neue&family=Open+Sans:wght@400;600&display=swap" rel="stylesheet">
<style>
  :root {
    --navy: #263a8e;
    --navy-deep: #1d2d75;
    --navy-soft: #8b93c9;
    --ink: #1b1b2a;
    --paper: #ffffff;
    --board: #e8e8e8;
    --frame: #c9c9c9;
  }
  * { margin: 0; padding: 0; box-sizing: border-box; }
  html, body { width: 1200px; height: 721px; overflow: hidden; background: var(--board); }
  .board { position: relative; width: 1200px; height: 721px; }
  .board-frame { position: absolute; left: 18px; top: 11px; width: 1164px; height: 693px; border: 1px solid var(--frame); }

  .flyer { position: absolute; width: 307px; height: 434px; background: var(--paper); overflow: hidden; font-family: "Open Sans", sans-serif; }
  .flyer--commercial { left: 98px; top: 190px; }
  .flyer--civil { left: 433px; top: 138px; }
  .flyer--industrial { left: 762px; top: 86px; }

  .hero { position: absolute; left: 0; top: 0; width: 307px; height: 248px; display: block; }

  .brand { position: absolute; left: 186px; top: 148px; width: 108px; text-align: center; }
  .brand-row { display: flex; align-items: center; justify-content: center; gap: 4px; }
  .brand-mark { width: 13px; height: 13px; background: var(--navy); }
  .brand-name { font-family: "Bebas Neue", sans-serif; font-size: 24px; line-height: 1; color: var(--navy); letter-spacing: 0.5px; }
  .brand-sub { font-family: "Bebas Neue", sans-serif; font-size: 8.5px; color: var(--ink); letter-spacing: 0.6px; margin-top: -1px; padding-left: 14px; }

  .title-band { position: absolute; left: 0; top: 248px; width: 307px; height: 56px; background: var(--navy); color: var(--paper); text-align: center; padding-top: 9px; }
  .title-band h1 { font-family: "Bebas Neue", sans-serif; font-weight: 400; font-size: 25px; line-height: 1; letter-spacing: 1.6px; }
  .title-band p { font-size: 5.4px; line-height: 1.35; margin: 3px auto 0; width: 270px; }

  .lists { position: absolute; left: 36px; top: 318px; width: 260px; display: flex; gap: 0; }
  .list { width: 130px; }
  .list h2 { font-family: "Bebas Neue", sans-serif; font-weight: 400; font-size: 12.5px; color: var(--ink); letter-spacing: 0.3px; line-height: 1; margin-bottom: 3px; }
  .list ul { list-style: none; }
  .list li { font-size: 6.2px; color: var(--navy-deep); line-height: 11px; padding-left: 12px; position: relative; white-space: nowrap; }
  .list li::before { content: ""; position: absolute; left: 0; top: 3.5px; width: 4px; height: 4px; border: 1px solid var(--ink); }

  .contact-bar { position: absolute; left: 0; top: 414px; width: 307px; height: 20px; background: var(--navy); }
  .contact { position: absolute; top: -8px; width: 100px; text-align: center; color: var(--paper); font-size: 4.6px; }
  .contact svg { display: block; margin: 0 auto 2px; }
  .contact--phone { left: 10px; }
  .contact--mail { left: 103px; }
  .contact--web { left: 197px; }
</style>
</head>
<body>
<div class="board">
  <div class="board-frame"></div>

  <!-- Commercial -->
  <article class="flyer flyer--commercial">
    <svg class="hero" viewBox="0 0 307 248" aria-hidden="false">
      <defs>
        <linearGradient id="photo-commercial" x1="0" y1="0" x2="0" y2="1">
          <stop offset="0" stop-color="#8fbbe8"/>
          <stop offset="0.35" stop-color="#a9574a"/>
          <stop offset="0.75" stop-color="#8e4a3d"/>
          <stop offset="1" stop-color="#c9b89a"/>
        </linearGradient>
      </defs>
      <rect width="307" height="248" fill="var(--navy)"/>
      <polygon points="0,165 60,225 0,248" fill="var(--navy-soft)" opacity="0.55"/>
      <polygon points="307,115 240,180 255,195 307,143" fill="var(--navy-soft)" opacity="0.5"/>
      <g role="img" aria-label="Photo of a red brick campus building under renovation">
        <polygon points="0,0 307,0 307,92 146,246 0,150" fill="url(#photo-commercial)"/>
      </g>
      <path d="M6 6 H36 M6 6 V58" stroke="#9aa2d2" stroke-width="5" fill="none" opacity="0.7"/>
      <rect x="190" y="99" width="100" height="100" rx="8" transform="rotate(45 240 149)" fill="var(--paper)"/>
    </svg>
    <div class="brand">
      <div class="brand-row"><span class="brand-mark"></span><span class="brand-name">HARWELL</span></div>
      <div class="brand-sub">CONSTRUCTION</div>
    </div>
    <div class="title-band">
      <h1>COMMERCIAL SOLUTIONS</h1>
      <p>We Not Only Know How All The Parts And Pieces Fit Together Within A Project, But We Specialize In The Self Performance Of Many Divisions Which Differentiates Us From Many Other General Contractors.</p>
    </div>
    <div class="lists">
      <section class="list">
        <h2>COMMERCIAL EXPERIENCE</h2>
        <ul>
          <li>Hollister Vale University</li>
          <li>Corvane Office Of Facilities</li>
          <li>Town Of Branwick, Corvane</li>
          <li>Town Of Eldermoor, Corvane</li>
          <li>Academic Regents Council</li>
        </ul>
      </section>
      <section class="list">
        <h2>COMMERCIAL FOCUS AREAS</h2>
        <ul>
          <li>New Construction</li>
          <li>Renovations</li>
          <li>Structural Foundations</li>
          <li>Structural Upgrades</li>
        </ul>
      </section>
    </div>
    <footer class="contact-bar">
      <div class="contact contact--phone"><svg width="11" height="11" viewBox="0 0 11 11"><rect width="11" height="11" fill="var(--navy)"/><path d="M3 2.5 L4.5 2.5 L5 4 L4.2 4.7 Q5 6.3 6.3 6.8 L7 6 L8.5 6.5 L8.5 8 Q4 8.5 3 2.5Z" fill="var(--paper)"/></svg>+123 555 0147</div>
      <div class="contact contact--mail"><svg width="11" height="11" viewBox="0 0 11 11"><rect width="11" height="11" fill="var(--navy)"/><rect x="2" y="3" width="7" height="5" fill="var(--paper)"/><path d="M2 3 L5.5 6 L9 3" stroke="var(--navy)" stroke-width="0.7" fill="none"/></svg>info@harwellbuild.com</div>
      <div class="contact contact--web"><svg width="11" height="11" viewBox="0 0 11 11"><rect width="11" height="11" fill="var(--navy)"/><circle cx="5.5" cy="5.5" r="3.2" stroke="var(--paper)" stroke-width="0.8" fill="none"/><path d="M2.3 5.5 H8.7 M5.5 2.3 V8.7" stroke="var(--paper)" stroke-width="0.6"/></svg>www.harwellbuild.com</div>
    </footer>
  </article>

  <!-- Civil -->
  <article class="flyer flyer--civil">
    <svg class="hero" viewBox="0 0 307 248">
      <defs>
        <linearGradient id="photo-civil" x1="0" y1="0" x2="0" y2="1">
          <stop offset="0" stop-color="#9cc3e6"/>
          <stop offset="0.4" stop-color="#d9dde2"/>
          <stop offset="0.6" stop-color="#9aa0a6"/>
          <stop offset="1" stop-color="#c6c6c2"/>
        </linearGradient>
      </defs>
      <rect width="307" height="248" fill="var(--navy)"/>
      <polygon points="0,150 70,218 58,230 0,172" fill="var(--navy-soft)" opacity="0.55"/>
      <polygon points="307,115 240,180 255,195 307,143" fill="var(--navy-soft)" opacity="0.5"/>
      <g role="img" aria-label="Photo of passenger jets parked on a concrete airfield apron">
        <polygon points="0,0 307,0 307,92 146,246 0,150" fill="url(#photo-civil)"/>
      </g>
      <path d="M6 6 H50 M6 6 V52" stroke="#9aa2d2" stroke-width="5" fill="none" opacity="0.7"/>
      <rect x="190" y="99" width="100" height="100" rx="8" transform="rotate(45 240 149)" fill="var(--paper)"/>
    </svg>
    <div class="brand">
      <div class="brand-row"><span class="brand-mark"></span><span class="brand-name">HARWELL</span></div>
      <div class="brand-sub">CONSTRUCTION</div>
    </div>
    <div class="title-band">
      <h1>CIVIL SOLUTIONS</h1>
      <p>We Specialize In Complex Civil Projects</p>
    </div>
    <div class="lists">
      <section class="list">
        <h2>CIVIL EXPERIENCE</h2>
        <ul>
          <li>Corvane Dept. Of Transportation</li>
          <li>Wexlow Dept. Of Transportation</li>
          <li>Taverly Dept. Of Transportation</li>
          <li>Builders Guild Board</li>
          <li>National Flight Safety Office</li>
          <li>Ministry Of Guardianship</li>
        </ul>
      </section>
      <section class="list">
        <h2>CIVIL FOCUS AREAS</h2>
        <ul>
          <li>Airfield</li>
          <li>Streetscapes</li>
          <li>Storm Drainage</li>
          <li>Utility Upgrades</li>
          <li>Box Culverts</li>
          <li>Retaining Walls</li>
        </ul>
      </section>
    </div>
    <footer class="contact-bar">
      <div class="contact contact--phone"><svg width="11" height="11" viewBox="0 0 11 11"><rect width="11" height="11" fill="var(--navy)"/><path d="M3 2.5 L4.5 2.5 L5 4 L4.2 4.7 Q5 6.3 6.3 6.8 L7 6 L8.5 6.5 L8.5 8 Q4 8.5 3 2.5Z" fill="var(--paper)"/></svg>+123 555 0147</div>
      <div class="contact contact--mail"><svg width="11" height="11" viewBox="0 0 11 11"><rect width="11" height="11" fill="var(--navy)"/><rect x="2" y="3" width="7" height="5" fill="var(--paper)"/><path d="M2 3 L5.5 6 L9 3" stroke="var(--navy)" stroke-width="0.7" fill="none"/></svg>info@harwellbuild.com</div>
      <div class="contact contact--web"><svg width="11" height="11" viewBox="0 0 11 11"><rect width="11" height="11" fill="var(--navy)"/><circle cx="5.5" cy="5.5" r="3.2" stroke="var(--paper)" stroke-width="0.8" fill="none"/><path d="M2.3 5.5 H8.7 M5.5 2.3 V8.7" stroke="var(--paper)" stroke-width="0.6"/></svg>www.harwellbuild.com</div>
    </footer>
  </article>

  <!-- Industrial -->
  <article class="flyer flyer--industrial">
    <svg class="hero" viewBox="0 0 307 248">
      <defs>
        <linearGradient id="photo-industrial" x1="0" y1="0" x2="0" y2="1">
          <stop offset="0" stop-color="#a9c8e4"/>
          <stop offset="0.3" stop-color="#e4e6e8"/>
          <stop offset="0.6" stop-color="#a39a8c"/>
          <stop offset="1" stop-color="#4f6b34"/>
        </linearGradient>
      </defs>
      <rect width="307" height="248" fill="var(--navy)"/>
      <polygon points="0,150 70,218 58,230 0,172" fill="var(--navy-soft)" opacity="0.55"/>
      <polygon points="307,70 240,135 250,145 307,88" fill="var(--navy-soft)" opacity="0.5"/>
      <g role="img" aria-label="Photo of a power plant with cooling towers and green foreground">
        <polygon points="0,0 307,0 307,92 146,246 0,150" fill="url(#photo-industrial)"/>
      </g>
      <path d="M6 6 H50 M6 6 V52" stroke="#9aa2d2" stroke-width="5" fill="none" opacity="0.7"/>
      <rect x="190" y="99" width="100" height="100" rx="8" transform="rotate(45 240 149)" fill="var(--paper)"/>
    </svg>
    <div class="brand">
      <div class="brand-row"><span class="brand-mark"></span><span class="brand-name">HARWELL</span></div>
      <div class="brand-sub">CONSTRUCTION</div>
    </div>
    <div class="title-band">
      <h1>INDUSTRIAL SOLUTIONS</h1>
      <p>We Maintain An Extensive Level Of Detail And Innovative Problem Solving Talents To Deliver Highquality, Sustainable Solutions.</p>
    </div>
    <div class="lists">
      <section class="list">
        <h2>INDUSTRIAL EXPERIENCE</h2>
        <ul>
          <li>Bravemoor Utilities</li>
          <li>Velkar</li>
          <li>Graywick Quarry</li>
          <li>Odell Forgeworks</li>
          <li>Pellman Crystalline</li>
          <li>Harrowgate &amp; Dunmore Rail Line</li>
        </ul>
      </section>
      <section class="list">
        <h2>INDUSTRIAL FOCUS AREAS</h2>
        <ul>
          <li>Plant Facility Water Systems</li>
          <li>Heavy Concrete</li>
          <li>Facility Repair</li>
          <li>Industrial Upgrades</li>
          <li>Railways And Manufacturing</li>
        </ul>
      </section>
    </div>
    <footer class="contact-bar">
      <div class="contact contact--phone"><svg width="11" height="11" viewBox="0 0 11 11"><rect width="11" height="11" fill="var(--navy)"/><path d="M3 2.5 L4.5 2.5 L5 4 L4.2 4.7 Q5 6.3 6.3 6.8 L7 6 L8.5 6.5 L8.5 8 Q4 8.5 3 2.5Z" fill="var(--paper)"/></svg>+123 555 0147</div>
      <div class="contact contact--mail"><svg width="11" height="11" viewBox="0 0 11 11"><rect width="11" height="11" fill="var(--navy)"/><rect x="2" y="3" width="7" height="5" fill="var(--paper)"/><path d="M2 3 L5.5 6 L9 3" stroke="var(--navy)" stroke-width="0.7" fill="none"/></svg>info@harwellbuild.com</div>
      <div class="contact contact--web"><svg width="11" height="11" viewBox="0 0 11 11"><rect width="11" height="11" fill="var(--navy)"/><circle cx="5.5" cy="5.5" r="3.2" stroke="var(--paper)" stroke-width="0.8" fill="none"/><path d="M2.3 5.5 H8.7 M5.5 2.3 V8.7" stroke="var(--paper)" stroke-width="0.6"/></svg>www.harwellbuild.com</div>
    </footer>
  </article>
</div>
</body>
</html>
```